Velimko AdAgency Presentation

We need ppt design for an ad agency re-branding, agency is based in Moscow, Russia. Our specifics is brand audit, consulting and strategy in web and offline.
We decided to do re-branding because our current agency does not answer the purpose and we need a kind of "second breath".
The idea of re-branding appeared because of many changes that happened in company: new clients, new projects level, new team.
So we'd like to promote company of changes and design should show this spirit as possible.
You may use info in attached pdf file (sorry for Russian language). Info is not so necessary, it will be replaced later.
Updates

Please use more colors than digital blue and grey!

Industry/Entity Type

Ad Agency

Requirements
Must have
• Logo is attached. Please choose one.

Ppt project should include:
- Front and last page design
- Heading and list design
- Page-separator design
- Diagram design
- Pics appearance

```html
<!DOCTYPE html>
<html lang="en">
<head>
<meta charset="utf-8">
<title>Velimko — Sample Presentation</title>
<link rel="stylesheet" href="https://fonts.googleapis.com/css2?family=Jost:wght@400;500&family=Didact+Gothic&display=swap">
<style>
  :root {
    --cream-top: #efede2;
    --cream-bottom: #f5f5ef;
    --charcoal: #2e2e32;
    --charcoal-light: #3b3b3f;
    --ink: #3a3a3a;
    --accent-blue: #1aa9e1;
    --accent-orange: #f39a1e;
    --accent-magenta: #d8337a;
    --accent-green: #7dbb3c;
    --body-grey: #8a8a8a;
    --brand-grey: #8e9599;
    --white: #ffffff;
  }
  * { margin: 0; padding: 0; box-sizing: border-box; }
  html, body { width: 1200px; height: 901px; overflow: hidden; }
  body { font-family: "Didact Gothic", sans-serif; }
  .slide { position: relative; width: 1200px; height: 901px; overflow: hidden; }
  .slide-head {
    position: absolute; left: 0; top: 0; width: 1200px; height: 496px;
    background: linear-gradient(180deg, var(--cream-top), var(--cream-bottom));
  }
  .slide-title {
    position: absolute; left: 62px; top: 86px;
    font-family: "Jost", sans-serif; font-weight: 500;
    font-size: 84px; line-height: 1; letter-spacing: -0.5px;
    color: var(--ink); white-space: nowrap;
  }
  .slide-title .highlight { color: var(--accent-blue); font-weight: 400; }
  .slide-intro {
    position: absolute; left: 77px; top: 218px; width: 576px;
    font-size: 22px; line-height: 28px; letter-spacing: 0.4px;
    color: var(--body-grey); text-align: justify;
  }
  .slide-foot {
    position: absolute; left: 0; top: 496px; width: 1200px; height: 380px;
    background: radial-gradient(ellipse at 60% 30%, var(--charcoal-light), var(--charcoal) 70%);
    border-top: 2px solid #232326;
  }
  .brand-mark {
    position: absolute; left: 109px; top: 78px; width: 140px; height: 140px;
    background: var(--accent-orange); border-radius: 6px;
  }
  .brand-name {
    position: absolute; left: 60px; top: 280px;
    font-family: "Didact Gothic", sans-serif; font-size: 58px; line-height: 1;
    color: var(--brand-grey);
  }
  .office { position: absolute; left: 792px; top: 277px; }
  .office-label {
    font-family: "Jost", sans-serif; font-weight: 500;
    font-size: 20px; color: var(--accent-blue); line-height: 24px;
  }
  .office-address { font-size: 19px; color: var(--white); line-height: 24px; }
  .accent-bar {
    position: absolute; left: 0; top: 876px; width: 1200px; height: 25px;
    display: flex;
  }
  .accent-bar span { flex: 1; }
  .accent-bar .blue { flex: 4; background: var(--accent-blue); }
  .accent-bar .orange { background: var(--accent-orange); }
  .accent-bar .magenta { background: var(--accent-magenta); }
  .accent-bar .green { background: var(--accent-green); }
</style>
</head>
<body>
  <main class="slide">
    <section class="slide-head">
      <h1 class="slide-title">Sample <span class="highlight">Presentation</span></h1>
      <p class="slide-intro">Lorem Ipsum is simply dummy text&nbsp; Lorem Ipsum has been the industry's standard dummy text ever. So the Velimko Presentation&nbsp; Description will go here</p>
    </section>
    <footer class="slide-foot">
      <div class="brand-mark"></div>
      <div class="brand-name">Velimko</div>
      <div class="office">
        <p class="office-label">Corporate Office</p>
        <p class="office-address">Velimko’s office address will go here</p>
      </div>
    </footer>
    <div class="accent-bar">
      <span class="blue"></span><span class="orange"></span><span class="magenta"></span><span class="green"></span>
    </div>
  </main>
</body>
</html>
```